KVR Noblesville Sign

I need to have a sign designed for a new self-storage facility we are going to be opening. The sign will be 4'W X 8'H.

Industry/Entity Type

Self Storage

Requirements
Must have
• Harbor Locker Yard logo at the top of the sign, under the logo I want the rendering.
• I also must have this information on the sign:
• 1. OPENING FALL 2016
• 2. Your premier self-storage facility.
• 3. www.harborlockeryard.example

```html
<!DOCTYPE html>
<html lang="en">
<head>
<meta charset="utf-8">
<title>Harbor Locker Yard – Opening Fall 2016 Sign</title>
<link rel="stylesheet" href="https://fonts.googleapis.com/css2?family=Anton&family=Open+Sans:wght@700&family=Oswald:wght@700&display=swap">
<style>
  :root {
    --sign-red: #e31e24;
    --sign-red-light: #ee2a2f;
    --sign-yellow: #fff200;
    --sign-green: #00a651;
    --sky-top: #4f9fdc;
    --sky-bottom: #a9d4f2;
    --ground-tan: #c9b28a;
    --ink-navy: #0f1a2c;
    --shadow-black: #1a1a1a;
  }
  html, body {
    margin: 0;
    padding: 0;
    width: 686px;
    height: 1200px;
    overflow: hidden;
    background: #ffffff;
  }
  .sign {
    position: relative;
    width: 686px;
    height: 1200px;
    overflow: hidden;
    background: var(--sign-red);
  }
  .rendering-area {
    position: absolute;
    left: 0;
    top: 300px;
    width: 686px;
    height: 840px;
    background: linear-gradient(180deg, var(--sky-top) 0%, var(--sky-bottom) 62%, var(--ground-tan) 88%, #a89a6a 100%);
  }
  .sign-bands {
    position: absolute;
    left: 0;
    top: 0;
  }
  .headline {
    position: absolute;
    left: 0;
    width: 686px;
    margin: 0;
    text-align: center;
    font-family: "Anton", "Impact", sans-serif;
    font-weight: 400;
    color: var(--sign-yellow);
    text-shadow: 4px 4px 0 var(--shadow-black);
    line-height: 1;
  }
  .headline__season {
    top: 42px;
    font-size: 90px;
    letter-spacing: 1px;
  }
  .headline__year {
    top: 120px;
    font-size: 200px;
  }
  .tagline {
    position: absolute;
    top: 372px;
    left: 0;
    width: 686px;
    margin: 0;
    text-align: center;
    font-family: "Open Sans", "Arial", sans-serif;
    font-weight: 700;
    font-size: 40px;
    line-height: 50px;
    color: var(--ink-navy);
  }
  .brand-name {
    position: absolute;
    top: 505px;
    left: 0;
    width: 686px;
    margin: 0;
    text-align: center;
    font-family: "Anton", "Impact", sans-serif;
    font-weight: 400;
    font-size: 92px;
    line-height: 112px;
    color: var(--sign-red);
  }
  .web-address {
    position: absolute;
    top: 1128px;
    left: 0;
    width: 686px;
    margin: 0;
    text-align: center;
    font-family: "Oswald", "Arial Narrow", sans-serif;
    font-weight: 700;
    font-size: 38px;
    line-height: 1;
    color: var(--sign-yellow);
  }
</style>
</head>
<body>
  <main class="sign">
    <div class="rendering-area" role="img" aria-label="Architectural rendering of the new two-storey self-storage building with tan walls, green roll-up doors and blue sky"></div>

    <svg class="sign-bands" width="686" height="1200" viewBox="0 0 686 1200" aria-hidden="true">
      <polygon points="0,0 686,0 686,300 0,372" fill="var(--sign-red)"/>
      <polygon points="0,292 520,330 0,372" fill="var(--sign-red-light)"/>
      <polygon points="380,341 686,300 686,378" fill="var(--sign-green)"/>
      <polygon points="0,1062 430,1082 0,1135" fill="var(--sign-green)"/>
      <polygon points="0,1135 686,1045 686,1200 0,1200" fill="var(--sign-red)"/>
      <polygon points="260,1101 686,1045 686,1090" fill="var(--sign-red-light)"/>
    </svg>

    <h1 class="headline headline__season">OPENING FALL</h1>
    <p class="headline headline__year">2016</p>

    <p class="tagline">Your Premier<br>Self-storage Facility.</p>

    <p class="brand-name">Harbor<br>Locker<br>Yard</p>

    <p class="web-address">www.HarborLockerYard.example</p>
  </main>
</body>
</html>
```